The Perfect Business Card for PineHarbor

I am looking for a business card which beautifully incorporates my logo, reflects my business and looks special, elegant and clean.

```html
<!DOCTYPE html>
<html lang="en">
<head>
<meta charset="utf-8">
<title>PineHarbor Business Card</title>
<link rel="stylesheet" href="https://fonts.googleapis.com/css2?family=Cinzel:wght@400;700&family=Libre+Baskerville&display=swap">
<style>
  :root {
    --page-bg: #e7e7e7;
    --green-dark: #546b2f;
    --green-light: #7c9c44;
    --icon-green: #b5d88a;
    --ink-white: #ffffff;
    --ink-black: #000000;
    --card-shadow: rgba(0, 0, 0, 0.55);
  }
  * { margin: 0; padding: 0; box-sizing: border-box; }
  html, body {
    width: 1200px;
    height: 1085px;
    overflow: hidden;
    background: var(--page-bg);
  }
  .canvas {
    position: relative;
    width: 1200px;
    height: 1085px;
  }
  .card {
    position: absolute;
    left: 301px;
    width: 578px;
    height: 343px;
    overflow: hidden;
    box-shadow: 2px 2px 1px var(--card-shadow);
  }
  .card-front { top: 163px; background: var(--green-dark); }
  .card-back { top: 542px; background: var(--ink-black); }

  .front-band {
    position: absolute;
    top: 0;
    right: 0;
    width: 102px;
    height: 100%;
    background: var(--green-light);
  }
  .brand-name {
    position: absolute;
    font-family: "Cinzel", serif;
    font-weight: 400;
    white-space: nowrap;
  }
  .card-front .brand-name {
    left: 44px;
    top: 44px;
    font-size: 36px;
    color: var(--ink-white);
  }
  .person {
    position: absolute;
    left: 38px;
    top: 136px;
    color: var(--ink-white);
  }
  .person-name {
    font-family: "Cinzel", serif;
    font-weight: 700;
    font-size: 24px;
    letter-spacing: 0.5px;
    line-height: 1;
  }
  .person-role {
    font-family: "Libre Baskerville", serif;
    font-size: 15px;
    margin-left: 2px;
    margin-top: 4px;
  }
  .contact-list {
    position: absolute;
    left: 38px;
    top: 200px;
    list-style: none;
    font-family: "Libre Baskerville", serif;
    font-size: 15.5px;
    color: var(--ink-white);
  }
  .contact-list li {
    display: flex;
    align-items: center;
    height: 20.5px;
  }
  .contact-icon {
    width: 14px;
    height: 14px;
    margin-right: 7px;
    flex: none;
  }
  .address {
    position: absolute;
    left: 39px;
    top: 277px;
    font-family: "Libre Baskerville", serif;
    font-style: normal;
    font-size: 15.5px;
    line-height: 20.5px;
    color: var(--ink-white);
  }

  .card-back .brand-name {
    left: 0;
    width: 100%;
    top: 108px;
    text-align: center;
    font-size: 44px;
    color: var(--green-dark);
  }
  .back-band {
    position: absolute;
    left: 0;
    top: 267px;
    width: 100%;
    height: 44px;
    background: var(--green-light);
    display: flex;
    align-items: center;
    justify-content: center;
    font-family: "Cinzel", serif;
    font-weight: 700;
    font-size: 17px;
    letter-spacing: 4.5px;
    color: var(--ink-black);
  }
</style>
</head>
<body>
<main class="canvas">
  <section class="card card-front" aria-label="Business card front">
    <div class="front-band"></div>
    <div class="brand-name">PineHarbor</div>
    <div class="person">
      <div class="person-name">DARREN HOLT</div>
      <div class="person-role">Managing&nbsp; Director</div>
    </div>
    <ul class="contact-list">
      <li>
        <svg class="contact-icon" viewBox="0 0 16 16" aria-hidden="true">
          <path d="M3 1.5l2.5 0 1.2 3.2-1.6 1.2c.8 1.8 2.2 3.2 4 4l1.2-1.6 3.2 1.2v2.5c0 .8-.7 1.5-1.5 1.5C6.6 13.5 2.5 9.4 1.5 3 1.5 2.2 2.2 1.5 3 1.5z" fill="var(--icon-green)"/>
        </svg>
        055-987 654 321
      </li>
      <li>
        <svg class="contact-icon" viewBox="0 0 16 16" aria-hidden="true">
          <rect x="1" y="3.5" width="14" height="9" fill="var(--icon-green)"/>
          <path d="M1 3.5l7 5.5 7-5.5" fill="none" stroke="var(--green-dark)" stroke-width="1.2"/>
        </svg>
        hello@pineharbor.com
      </li>
      <li>
        <svg class="contact-icon" viewBox="0 0 16 16" aria-hidden="true">
          <g fill="none" stroke="var(--icon-green)" stroke-width="1.3">
            <circle cx="8" cy="8" r="6.5"/>
            <ellipse cx="8" cy="8" rx="3" ry="6.5"/>
            <path d="M1.5 8h13M2.5 4.8h11M2.5 11.2h11"/>
          </g>
        </svg>
        www.pineharbor.com
      </li>
    </ul>
    <address class="address">
      48, Cedar Lane<br>
      Country name, 123456
    </address>
  </section>

  <section class="card card-back" aria-label="Business card back">
    <div class="brand-name">PineHarbor</div>
    <div class="back-band">WWW.PINEHARBOR.COM</div>
  </section>
</main>
</body>
</html>
```